Need Business Card for eLearning Company

Need a business card designed for our company, CareerTrellon.

CareerTrellon has developed a complete 12 lesson eLearning course to teach you the skills you need to present yourself in a job interview. The course uses advanced learning techniques in the multimedia videos, plus contains quizzes and additional exercises to insure you get the course and can walk into any interview with confidence and ease, and get the job.

www.careertrellon.com

Attached is our logo

Industry/Entity Type

Business

```html
<!DOCTYPE html>
<html lang="en">
<head>
<meta charset="utf-8">
<title>CareerTrellon Business Card</title>
<link href="https://fonts.googleapis.com/css2?family=Crimson+Text:wght@400;600&display=swap" rel="stylesheet">
<style>
  :root {
    --backdrop: #2a2a2a;
    --card-dark: #36322f;
    --card-light: #eeeeee;
    --ink: #2b2b2b;
    --ink-soft: #3a3a3a;
    --white: #ffffff;
    --plum: #9b2a86;
    --leaf: #8cc63f;
  }
  * { margin: 0; padding: 0; box-sizing: border-box; }
  html, body {
    width: 1200px; height: 900px; overflow: hidden;
    background: var(--backdrop);
    font-family: "Crimson Text", Georgia, serif;
  }
  .stage {
    position: relative; width: 1200px; height: 900px;
  }
  .card {
    position: absolute; top: 300px;
    width: 525px; height: 300px;
    box-shadow: 0 12px 30px rgba(0,0,0,0.45);
  }
  .card--front { left: 50px; background: var(--card-dark); }
  .card--back { left: 625px; background: var(--card-light); color: var(--ink); }

  .brand {
    display: flex; align-items: center; gap: 12px;
  }
  .brand-dot {
    width: 26px; height: 26px; border-radius: 50%;
    background: var(--leaf);
  }
  .brand-name { font-weight: 600; letter-spacing: 0.5px; }

  .card--front .brand {
    position: absolute; left: 0; right: 0; top: 120px;
    justify-content: center;
  }
  .card--front .brand-name { color: var(--white); font-size: 44px; }

  .card--back .brand { position: absolute; left: 34px; top: 38px; }
  .card--back .brand-dot { width: 20px; height: 20px; }
  .card--back .brand-name { color: var(--ink); font-size: 32px; }

  .contact {
    position: absolute; left: 34px; top: 130px;
    font-size: 15px; line-height: 19px; color: var(--ink-soft);
  }
  .contact .gap { height: 10px; }
  .accent-plum { color: var(--plum); }
  .accent-leaf { color: var(--leaf); }

  .address {
    position: absolute; left: 270px; top: 210px;
    font-size: 15px; line-height: 19px; color: var(--ink-soft);
  }
</style>
</head>
<body>
<main class="stage">
  <section class="card card--front">
    <div class="brand">
      <span class="brand-dot"></span>
      <span class="brand-name">CareerTrellon</span>
    </div>
  </section>

  <section class="card card--back">
    <div class="brand">
      <span class="brand-dot"></span>
      <span class="brand-name">CareerTrellon</span>
    </div>
    <div class="contact">
      <p>US: (555) 014 - 2738</p>
      <p>International: (65) 5550 - 1842</p>
      <div class="gap"></div>
      <p><span class="accent-plum">support</span>@careertrellon.com</p>
      <p>www.<span class="accent-leaf">careertrellon</span>.com</p>
    </div>
    <address class="address" style="font-style:normal">
      <p>420 Harbor Vale Road Suite 12,</p>
      <p>Westbrook, WA 98000</p>
    </address>
  </section>
</main>
</body>
</html>
```